A brochure website design
Product: Nuvel coconut yogurt
Specialty of the product:
Nuvel coconut yogurt is a non dairy yogurt using coconut cream powder and coconut water as its major ingredients. It contains live cultures and is a great alternatives to dairy yogurt.
It is gluten free, soy free, preservative free, lactose free, non-GMO and no artificial sweetener. It is a great choice for paleo diet.
4. About Nuvel
Nuvel is developed by a group of coconut lovers who believe that promoting vegan based diet can contribute to the wellness of the world and the sustainability of living. Our vision is to end cruelty to animal and minimise the world’s reliance on milk farming. We believe that cow milk is belonged to cow BB and God has already provided coconut to us which is actually more suitable to human’s body than dairy product.
5. Our products
Nuvel coconut yogurt 120g
Nuvel coconut yogurt with raspberry 150g
6. Nuvel recipes
7. About coconut
8. Contact us
9. Stores finder
Target Market(s)
Age 18 to 50 . People looking for life style and healthy diet.
Industry/Entity Type
Product
Number of Pages Required
5+ page
Look and feel
Each slider illustrates characteristics of the customer's brand and the style your logo design should communicate.

```html
<!DOCTYPE html>
<html lang="en">
<head>
<meta charset="utf-8">
<title>Nuvel Coconut Yogurt</title>
<link rel="stylesheet" href="https://fonts.googleapis.com/css2?family=Arimo:wght@400&display=swap">
<style>
  :root {
    --teal: #00879a;
    --teal-deep: #2f6d78;
    --teal-photo: #3f7f88;
    --green: #118a2e;
    --green-text: #1f8a3a;
    --product-bg: #a3ccd3;
    --white: #ffffff;
    --ink: #111111;
  }
  * { margin: 0; padding: 0; box-sizing: border-box; }
  html, body { width: 1200px; height: 1200px; overflow: hidden; }
  body { position: relative; font-family: "Arimo", Helvetica, Arial, sans-serif; background: var(--white); color: var(--ink); }

  .site-nav { position: absolute; left: 0; top: 0; width: 1200px; height: 93px; background: var(--teal); }
  .site-nav a { position: absolute; top: 35px; color: var(--white); text-decoration: none; font-size: 19px; }
  .nav-home { left: 428px; }
  .nav-about { left: 565px; }
  .nav-contact { left: 722px; }

  .hero { position: absolute; left: 0; top: 93px; width: 1200px; height: 278px;
    background: linear-gradient(90deg, #3a7680 0%, #3f7f88 40%, #4f8c94 65%, #3f7e87 100%); }
  .hero-title { position: absolute; left: 150px; top: 66px; font-size: 24px; font-weight: 400; color: var(--white); }
  .hero-tagline { position: absolute; left: 150px; top: 125px; font-size: 19px; color: var(--white); }
  .hero-button { position: absolute; left: 150px; top: 177px; width: 246px; height: 50px; background: var(--green);
    color: var(--white); font-size: 22px; display: flex; align-items: center; justify-content: center; border-radius: 2px; }

  .intro-text { position: absolute; left: 94px; top: 452px; width: 400px; }
  .intro-text h2 { font-size: 22px; font-weight: 400; color: var(--teal); margin-bottom: 27px; }
  .intro-text p { font-size: 19px; line-height: 24px; margin-bottom: 24px; }

  .about { position: absolute; left: 0; top: 804px; width: 1200px; height: 326px; background: var(--teal); color: var(--white); }
  .about h2 { position: absolute; left: 101px; top: 52px; font-size: 24px; font-weight: 400; }
  .about p { position: absolute; left: 101px; top: 124px; width: 960px; font-size: 19px; line-height: 24px; }

  .product-photo { position: absolute; left: 582px; top: 371px; width: 618px; height: 463px;
    background: radial-gradient(ellipse at 52% 50%, #c3e1e5 0%, #a9d0d6 45%, var(--product-bg) 100%); }
  .recipe-photo { position: absolute; left: 0; top: 1102px; width: 618px; height: 98px;
    background: linear-gradient(90deg, #9dc6a6 0%, #b7d7b6 45%, #8fbf9b 100%); }
  .products-heading { position: absolute; left: 658px; top: 1188px; font-size: 24px; font-weight: 400; color: var(--green-text); white-space: nowrap; }
</style>
</head>
<body>
  <nav class="site-nav">
    <a class="nav-home" href="#">Home</a>
    <a class="nav-about" href="#">About Us</a>
    <a class="nav-contact" href="#">Contact</a>
  </nav>

  <header class="hero" role="img" aria-label="Bowl of coconut yogurt with granola and berries under a teal overlay">
    <h1 class="hero-title">Nuvel Coconut Yogurt</h1>
    <p class="hero-tagline">Vegan. Healthy. Delicious.</p>
    <a class="hero-button">Find a Store</a>
  </header>

  <section class="intro-text">
    <h2>NUVEL</h2>
    <p>Nuvel coconut yogurt is a non dairy yogurt using coconut cream powder and coconut water as its major ingredients. It contains live cultures and is a great alternatives to dairy yogurt.</p>
    <p>It is gluten free, soy free, preservative free, lactose free, non-GMO and no artificial sweetener. It is a great choice for paleo diet.</p>
  </section>

  <section class="about">
    <h2>About Us</h2>
    <p>Nuvel is developed by a group of coconut lovers who believe that promoting vegan based diet can contribute to the wellness of the world and the sustainability of living. Our vision is to end cruelty to animal and minimise the world’s reliance on milk farming. We believe that cow milk is belonged to cow BB and God has already provided coconut to us which is actually more suitable to human’s body than dairy product.</p>
  </section>

  <div class="product-photo" role="img" aria-label="Cup of Nuvel coconut yogurt on a pale blue background"></div>
  <div class="recipe-photo" role="img" aria-label="Soft-focus photo of yogurt with berries"></div>
  <h2 class="products-heading">Available Products</h2>
</body>
</html>
```